Business Card Design for Engineering Firm

Need a business card design for small mechanical and plumbing engineering form based in Utah. Design should be customizable for all employees.

```html
<!DOCTYPE html>
<html lang="en">
<head>
<meta charset="utf-8">
<title>Ridgeline Engineering – Business Card</title>
<link rel="stylesheet" href="https://fonts.googleapis.com/css2?family=Montserrat:wght@700&family=Open+Sans:wght@400;600&display=swap">
<style>
  :root {
    --backdrop: #4a4a4a;
    --card: #1a1a1a;
    --card-deep: #121212;
    --red: #7e1519;
    --grey: #4f4f4f;
    --grey-light: #8a8a8a;
    --white: #f2f2f2;
    --emboss: #383838;
  }
  * { box-sizing: border-box; margin: 0; padding: 0; }
  html, body {
    width: 1200px; height: 801px; overflow: hidden;
    background: var(--backdrop);
  }
  .stage {
    width: 1200px; height: 801px;
    display: flex; align-items: center; justify-content: center; gap: 40px;
  }
  .card {
    position: relative;
    width: 540px; height: 309px;
    background: var(--card);
    border-bottom: 3px solid var(--red);
    overflow: hidden;
  }

  /* front */
  .hero-area {
    position: absolute; right: 0; top: 0;
    width: 270px; height: 250px;
    background: linear-gradient(135deg, var(--grey) 0%, var(--red) 45%, var(--red) 70%, var(--card) 100%);
    clip-path: polygon(20% 0, 100% 0, 100% 100%, 0 80%);
  }
  .brand {
    position: absolute; left: 28px; top: 30px;
    display: flex; align-items: center; gap: 14px;
  }
  .brand-square { width: 16px; height: 16px; background: var(--red); }
  .brand-divider { width: 1px; height: 44px; background: var(--grey); }
  .brand-name {
    font-family: "Montserrat", sans-serif; font-weight: 700;
    font-size: 20px; line-height: 1.1; letter-spacing: 1px;
    color: var(--red);
  }
  .accent-bar {
    position: absolute; left: 0; top: 138px;
    width: 14px; height: 30px; background: var(--red);
  }
  .person { position: absolute; left: 40px; top: 134px; }
  .person-name {
    font-family: "Montserrat", sans-serif; font-weight: 700;
    font-size: 22px; letter-spacing: 1px; color: var(--red);
  }
  .person-title {
    font-family: "Open Sans", sans-serif; font-size: 13px;
    color: var(--white); margin-top: 2px;
  }
  .contacts {
    position: absolute; left: 40px; top: 192px;
    list-style: none;
    font-family: "Open Sans", sans-serif; font-size: 12.5px; color: var(--white);
  }
  .contacts li { display: flex; align-items: center; gap: 8px; line-height: 20px; }
  .contacts svg { width: 12px; height: 12px; fill: var(--red); flex: none; }
  .address {
    position: absolute; left: 40px; top: 260px;
    font-family: "Open Sans", sans-serif; font-style: normal;
    font-size: 12.5px; line-height: 17px; color: var(--white);
  }

  /* back */
  .card-back { background: var(--card-deep); }
  .pattern-area {
    position: absolute; inset: 0;
    background: linear-gradient(160deg, #1e1e1e 0%, #161616 50%, #202020 100%);
  }
  .back-brand {
    position: absolute; right: 44px; top: 140px;
    display: flex; align-items: center; gap: 10px;
  }
  .back-brand .brand-square { background: var(--emboss); width: 14px; height: 14px; }
  .back-brand-name {
    font-family: "Montserrat", sans-serif; font-weight: 700;
    font-size: 16px; letter-spacing: 1px; color: var(--emboss);
  }
</style>
</head>
<body>
<main class="stage">

  <section class="card card-front">
    <div class="hero-area" role="img" aria-label="Large angular brand decoration in red and grey"></div>

    <div class="brand">
      <span class="brand-square"></span>
      <span class="brand-divider"></span>
      <span class="brand-name">RIDGELINE<br>ENGINEERING</span>
    </div>

    <span class="accent-bar"></span>
    <div class="person">
      <h1 class="person-name">DALE WARREN</h1>
      <p class="person-title">Managing Director</p>
    </div>

    <ul class="contacts">
      <li>
        <svg viewBox="0 0 24 24"><path d="M6.6 10.8a15 15 0 0 0 6.6 6.6l2.2-2.2c.3-.3.7-.4 1-.2 1.1.4 2.3.6 3.6.6.6 0 1 .4 1 1V20c0 .6-.4 1-1 1A17 17 0 0 1 3 4c0-.6.4-1 1-1h3.5c.6 0 1 .4 1 1 0 1.3.2 2.5.6 3.6.1.3 0 .7-.2 1z"/></svg>
        123 456 789
      </li>
      <li>
        <svg viewBox="0 0 24 24"><path d="M2 5h20v14H2zm2 2v.5l8 5 8-5V7l-8 5z"/></svg>
        info@youremail.com
      </li>
      <li>
        <svg viewBox="0 0 24 24"><path d="M12 2a10 10 0 1 0 0 20 10 10 0 0 0 0-20zm6.9 9h-3a15 15 0 0 0-1.3-5.6A8 8 0 0 1 18.9 11zM12 4c.9 1.2 1.7 3.9 1.9 7h-3.8c.2-3.1 1-5.8 1.9-7zM4.1 13h3a15 15 0 0 0 1.3 5.6A8 8 0 0 1 4.1 13zm3-2h-3a8 8 0 0 1 4.3-5.6A15 15 0 0 0 7.1 11zM12 20c-.9-1.2-1.7-3.9-1.9-7h3.8c-.2 3.1-1 5.8-1.9 7zm2.6-1.4a15 15 0 0 0 1.3-5.6h3a8 8 0 0 1-4.3 5.6z"/></svg>
        www.yourwebsite.com
      </li>
    </ul>

    <address class="address">Your address, City<br>State, Zip 1234</address>
  </section>

  <section class="card card-back">
    <div class="pattern-area" role="img" aria-label="Embossed repeating brand pattern in dark grey"></div>
    <div class="back-brand">
      <span class="brand-square"></span>
      <span class="back-brand-name">RIDGELINE ENGINEERING</span>
    </div>
  </section>

</main>
</body>
</html>
```